skin elixir serum with snail extract

I am working at a natural skincare company. We are going to launch a new product - a skin serum. completely natural, super concentrated, multi use (face, neck , eyes). But we need the packaging (box and bottle label) to be aligned to our brand's philosophy, design etc. (See more at pindomare.com)

Here's a more detailed description :
"Elevate your skincare routine with Brusquel Elixir, the ultimate one-drop wonder enriched with potent snail secretion. Experience the magic as our 100% natural serum transforms your face, eyes, décolleté, and neck. Get ready to say Wow to a new level of radiance!"

Target Market(s)

natural skincare enthusiasts - beauty pioneers

Industry/Entity Type

beauty - wellness

Requirements
Nice to have
• based on the overall brand philosophy (see pindomare.com)

```html
<!DOCTYPE html>
<html lang="en">
<head>
<meta charset="utf-8">
<title>Pindomare Skin Elixir Serum – Box Dieline and Bottle Label</title>
<link href="https://fonts.googleapis.com/css2?family=Didact+Gothic&family=Questrial&display=swap" rel="stylesheet">
<style>
  :root {
    --paper: #ffffff;
    --ink: #111111;
    --accent: #88f50f;
  }
  html, body { margin: 0; padding: 0; overflow: hidden; background: var(--paper); }
  .artboard { width: 1200px; height: 1200px; display: block; }
  .cut { fill: none; stroke: var(--ink); stroke-width: 2; }
  .fold { fill: none; stroke: var(--ink); stroke-width: 1.6; stroke-dasharray: 14 10; }
  .copy { font-family: "Didact Gothic", "Questrial", sans-serif; fill: var(--ink); letter-spacing: 0.06em; }
  .copy-tiny { font-size: 6.5px; letter-spacing: 0.02em; }
  .copy-small { font-size: 8.5px; letter-spacing: 0.03em; }
  .copy-body { font-size: 10.5px; }
  .copy-mid { font-size: 13px; letter-spacing: 0.1em; }
  .brand-name { font-family: "Questrial", sans-serif; fill: var(--ink); font-size: 36px; letter-spacing: 0; }
  .brand-name-small { font-size: 26px; }
  .bold { font-weight: 700; }
  .accent-band { fill: var(--accent); }
  .icon { fill: none; stroke: var(--ink); stroke-width: 1.6; }
  .icon-solid { fill: var(--ink); }
  .badge { fill: none; stroke: var(--ink); stroke-width: 1.5; }
</style>
</head>
<body>
<svg class="artboard" viewBox="0 0 1920 1920" xmlns="http://www.w3.org/2000/svg">

  <!-- ===== Box dieline: cut lines ===== -->
  <g class="box-cut">
    <path class="cut" d="M583 774 L583 440 Q583 418 605 418 L769 418 Q791 418 791 440 L791 774"/>
    <path class="cut" d="M999 774 L999 522 Q999 500 1021 500 L1185 500 Q1207 500 1207 522 L1207 774"/>
    <path class="cut" d="M999 1240 L999 1491 Q999 1513 1021 1513 L1185 1513 Q1207 1513 1207 1491 L1207 1240"/>
    <path class="cut" d="M791 774 L811 752 L843 680 Q850 665 866 665 L957 665 Q979 665 979 687 L979 752 L999 774"/>
    <path class="cut" d="M1207 774 L1227 752 L1227 687 Q1227 665 1249 665 L1340 665 Q1356 665 1363 680 L1395 752 L1415 774"/>
    <path class="cut" d="M791 1240 L811 1262 L843 1334 Q850 1349 866 1349 L957 1349 Q979 1349 979 1327 L979 1262 L999 1240"/>
    <path class="cut" d="M1207 1240 L1227 1262 L1227 1327 Q1227 1349 1249 1349 L1340 1349 Q1356 1349 1363 1334 L1395 1262 L1415 1240"/>
    <path class="cut" d="M583 774 L517 813 L517 1201 L583 1240"/>
    <path class="cut" d="M1415 774 L1415 1240"/>
    <circle class="cut" cx="687" cy="588" r="41"/>
  </g>

  <!-- ===== Box dieline: fold lines ===== -->
  <g class="box-fold">
    <line class="fold" x1="583" y1="484" x2="791" y2="484"/>
    <line class="fold" x1="583" y1="692" x2="791" y2="692"/>
    <line class="fold" x1="999" y1="566" x2="1207" y2="566"/>
    <line class="fold" x1="999" y1="1447" x2="1207" y2="1447"/>
    <line class="fold" x1="583" y1="774" x2="1415" y2="774"/>
    <line class="fold" x1="583" y1="1240" x2="1415" y2="1240"/>
    <line class="fold" x1="583" y1="774" x2="583" y2="1240"/>
    <line class="fold" x1="791" y1="774" x2="791" y2="1240"/>
    <line class="fold" x1="999" y1="774" x2="999" y2="1240"/>
    <line class="fold" x1="1207" y1="774" x2="1207" y2="1240"/>
  </g>

  <!-- ===== Top tuck flap brand name ===== -->
  <text class="brand-name" x="1103" y="686" text-anchor="middle" textLength="180" lengthAdjust="spacingAndGlyphs">pindomare</text>

  <!-- ===== Panel: usage and ingredients ===== -->
  <g class="panel-usage copy">
    <text class="copy-small" x="593" y="878">Keep in cool, dry place. Avoid direct sunlight.</text>
    <text class="copy-small" x="593" y="890">Close cap tightly after usage</text>
    <text class="copy-small bold" x="593" y="922">HOW TO USE :</text>
    <text class="copy-small" x="593" y="933">Apply 2-3 dropd and message into skin.</text>
    <text class="copy-small" x="593" y="944">Allow the serum to sink in few seconds</text>
    <text class="copy-small" x="593" y="955">before applying your other skin regimen.</text>
    <g class="copy-tiny">
      <text x="593" y="995"><tspan class="bold">Ingredients :</tspan> Aqua, Tea Tree Water,</text>
      <text x="593" y="1005">Jeju Cantella Asiatica, Vitamin C,Salicylic</text>
      <text x="593" y="1015">Acid, Liquorice Extract, Niacinamide,</text>
      <text x="593" y="1025">Polyacrylamide, Dimethicone,Sunflower</text>
      <text x="593" y="1035">(Helianthus annuus) seed oil, C13-14 isoparaffin,</text>
      <text x="593" y="1045">Laureth-7, Tocopherol, Phenoxyethanol,</text>
      <text x="593" y="1055">Ethylparaben, Methylparaben, Butylparaben,</text>
      <text x="593" y="1065">Propylparaben.</text>
    </g>
  </g>

  <!-- ===== Panel: description and maker ===== -->
  <g class="panel-maker copy">
    <g class="copy-tiny">
      <text x="805" y="796">Elevate your skincare routine with Brusquel Elixir,</text>
      <text x="805" y="812">the ultimate one-drop wonder enriched with potent</text>
      <text x="805" y="828">snail secretion.</text>
      <text x="805" y="844">Experience the magic as our 100% natural serum</text>
      <text x="805" y="860">transforms your face, eyes, décolleté, and neck.</text>
      <text x="805" y="876">Get ready to say Wow to a new level of radiance!</text>
    </g>
    <text class="copy-mid" x="805" y="1002">PINDOMARE.COM</text>
    <text class="copy-body" x="805" y="1074">Production by :</text>
    <text class="copy-body" x="805" y="1090">Pindomare</text>
    <text class="copy-body" x="805" y="1106">14 Lirnou Str</text>
    <text class="copy-body" x="805" y="1122">11742, Athens, Greece</text>
    <text class="copy-body" x="805" y="1138">GEMI 100234507000</text>
    <text class="copy-body" x="805" y="1154">Info@pindomare.com</text>
    <g class="care-icons">
      <path class="icon" d="M806 1198 L830 1198 L828 1210 L808 1210 Z"/>
      <path class="icon" d="M806 1195 L828 1187"/>
      <rect class="icon-solid" x="812" y="1201" width="12" height="6"/>
      <path class="icon" d="M841 1197 L851 1197 L849 1210 L843 1210 Z"/>
      <circle class="icon-solid" cx="857" cy="1190" r="3"/>
      <path class="icon-solid" d="M854 1195 L860 1195 L860 1204 L858.5 1210 L857 1210 L857 1204 L856 1210 L854 1210 Z"/>
      <circle class="icon-solid" cx="884" cy="1198" r="12"/>
    </g>
  </g>

  <rect class="accent-band" x="805" y="1024" width="388" height="15"/>

  <!-- ===== Front panel ===== -->
  <g class="panel-front copy">
    <text class="brand-name" x="1103" y="860" text-anchor="middle" textLength="180" lengthAdjust="spacingAndGlyphs">pindomare</text>
    <text class="copy-mid" x="1011" y="986">SNAIL</text>
    <text class="copy-mid" x="1011" y="1002">SECRETION</text>
    <text class="copy-mid" x="1011" y="1076">SKIN ELIXIR</text>
    <text class="copy-mid" x="1011" y="1093">SERUM</text>
    <text class="copy-small" x="1011" y="1112">FACE, NECK, &amp; EYES</text>
    <circle class="badge" cx="1159" cy="1092" r="28"/>
    <circle class="badge" cx="1159" cy="1092" r="17"/>
    <text class="copy-body" x="1014" y="1208">20 ml / 0.68 fl oz</text>
  </g>

  <!-- ===== Panel: warnings and batch ===== -->
  <g class="panel-warnings copy copy-body">
    <text x="1221" y="796">Attention !</text>
    <text x="1221" y="812">Stop use if irritation/allergy</text>
    <text x="1221" y="828">occurs.</text>
    <text x="1221" y="844">Keep out of reach of children.</text>
    <text x="1221" y="860">Store in a cool and dry place.</text>
    <text x="1221" y="876">Avoid exposure to direct sunlight.</text>
    <text x="1221" y="1178">NO. Batch</text>
    <text x="1221" y="1193">Code Production :</text>
    <text x="1221" y="1208">Exp. Date</text>
  </g>

  <!-- ===== Bottle label ===== -->
  <g class="bottle-label">
    <rect class="cut" x="666" y="1625" width="607" height="164"/>
    <text class="brand-name brand-name-small" x="682" y="1674" textLength="124" lengthAdjust="spacingAndGlyphs">pindomare</text>
    <g class="copy">
      <text class="copy-small" x="683" y="1710">SNAIL</text>
      <text class="copy-small" x="683" y="1720">SECRETION</text>
      <text class="copy-small" x="683" y="1752">SKIN ELIXIR</text>
      <text class="copy-small" x="683" y="1762">SERUM</text>
      <text class="copy-tiny" x="683" y="1776">FACE, NECK, &amp; EYES</text>
    </g>
    <rect class="accent-band" x="683" y="1727" width="116" height="9"/>
    <circle class="badge" cx="830" cy="1732" r="24"/>
    <circle class="badge" cx="830" cy="1732" r="14"/>
    <g class="copy">
      <text class="copy-tiny bold" x="881" y="1646">HOW TO USE :</text>
      <text class="copy-tiny" x="881" y="1656">Apply 2-3 dropd and message into skin.</text>
      <text class="copy-tiny" x="881" y="1666">Allow the serum to sink in few seconds</text>
      <text class="copy-tiny" x="881" y="1676">before applying your other skin regimen.</text>
      <text class="copy-small" x="881" y="1711">Production by :</text>
      <text class="copy-small" x="881" y="1723">Pindomare</text>
      <text class="copy-small" x="881" y="1736">14 Lirnou Str</text>
      <text class="copy-small" x="881" y="1748">11742, Athens, Greece</text>
      <text class="copy-small" x="881" y="1761">GEMI 100234507000</text>
      <text class="copy-small" x="881" y="1773">Info@pindomare.com</text>
      <text class="copy-small" x="1088" y="1677">NO. Batch</text>
      <text class="copy-small" x="1088" y="1692">Code Production :</text>
      <text class="copy-small" x="1088" y="1707">Exp. Date</text>
    </g>
    <g class="care-icons">
      <path class="icon" d="M1090 1758 L1114 1758 L1112 1770 L1092 1770 Z"/>
      <path class="icon" d="M1090 1755 L1112 1747"/>
      <rect class="icon-solid" x="1096" y="1761" width="12" height="6"/>
      <path class="icon" d="M1125 1757 L1135 1757 L1133 1770 L1127 1770 Z"/>
      <circle class="icon-solid" cx="1141" cy="1750" r="3"/>
      <path class="icon-solid" d="M1138 1755 L1144 1755 L1144 1764 L1142.5 1770 L1141 1770 L1141 1764 L1140 1770 L1138 1770 Z"/>
      <circle class="icon-solid" cx="1169" cy="1758" r="12"/>
    </g>
  </g>
</svg>
</body>
</html>
```